International Fleet Management Firm Website

HaulwaveKenro is a Fleet Management Company that provides insight into customers fleets. We do this through web tools which we have developed which function through a client login screen to help ensure that corporates are able to stay on top of their fleets 24/7.
We are about to launch and are looking for a great new website to help us come out with bang! We would like a site that matches our values of ; Courage, integrity and leadership.
Although we have developed the app. We would also like to redesign the look of the site on the back end.
(1) We need to incorporate the new corporate colours
(2) Would like to create a better user experience.
The site that I would like to model ours after is;
www.belvanmotors.com (usa version)
Good Luck!!
Updates
Jusst added the .png version of the logo. Hopes this helps!
Industry/Entity Type
It Company
Look and feel

```html
<!DOCTYPE html>
<html lang="en">
<head>
<meta charset="utf-8">
<title>HaulwaveKenro – Drivers</title>
<link href="https://fonts.googleapis.com/css2?family=Source+Sans+3:ital,wght@0,400;0,600;0,700;1,400&display=swap" rel="stylesheet">
<style>
:root{
  --blue:#1a7fd0;
  --blue-band-top:#1594ee;
  --blue-band-bottom:#0a6fcf;
  --link:#1d73c2;
  --text:#555;
  --muted:#777;
  --line:#dcdcdc;
  --panel:#f4f4f4;
  --footer:#555555;
  --tab-dark:#5b5b5b;
  --white:#fff;
}
*{box-sizing:border-box;margin:0;padding:0}
html,body{width:1200px;height:798px;overflow:hidden;background:var(--white);font-family:"Source Sans 3",Arial,sans-serif;color:var(--text)}
.page{position:relative;width:1200px;height:798px}

/* header */
.site-header{position:absolute;left:0;top:0;width:1200px;height:94px}
.brand{position:absolute;left:182px;top:42px;display:flex;align-items:center;gap:7px}
.brand-mark{width:16px;height:16px;background:var(--blue)}
.brand-name{font-size:24px;font-weight:700;color:var(--blue);letter-spacing:-.3px;line-height:1}
.header-btn{position:absolute;top:35px;height:28px;border:1px solid #c9c9c9;border-radius:3px;background:linear-gradient(#fafafa,#e4e4e4);display:flex;align-items:center;justify-content:center;gap:5px;font-size:12px;color:#666}
.header-btn svg{fill:#888}
.btn-alerts{left:771px;width:118px}
.btn-account{left:900px;width:118px}

/* navigation */
.main-nav{position:absolute;left:0;top:94px;width:1200px;height:87px;background:linear-gradient(var(--blue-band-top),var(--blue-band-bottom))}
.nav-item{position:absolute;top:0;height:87px;display:flex;flex-direction:column;align-items:center;justify-content:flex-start;color:var(--white);font-size:12.5px;transform:translateX(-50%)}
.nav-item svg{margin-top:22px;height:26px;width:26px;stroke:var(--white);fill:none;stroke-width:1.8}
.nav-item span{margin-top:8px}
.nav-item.is-active{left:244px;width:126px;background:linear-gradient(#6b6b6b,var(--tab-dark))}

/* sidebar */
.sidebar{position:absolute;left:180px;top:209px;width:251px}
.sidebar-title{height:29px;border:1px solid var(--line);background:linear-gradient(#fff,#efefef);padding:4px 15px;font-size:13.5px;color:var(--link)}
.sidebar-link{margin-top:4px;height:31px;border:1px solid var(--line);display:flex;align-items:center;justify-content:space-between;padding:0 13px 0 15px;font-size:11px;color:#666}
.sidebar-link svg{fill:#777}

/* content */
.content{position:absolute;left:454px;top:206px;width:566px}
.toolbar{height:47px;background:linear-gradient(#fff,#f1f1f1);border-bottom:1px solid #e3e3e3;position:relative}
.btn-add{position:absolute;left:20px;top:5px;width:196px;height:30px;border:1px solid #c3c3c3;border-radius:3px;background:linear-gradient(#fbfbfb,#e6e6e6);display:flex;align-items:center;justify-content:center;gap:6px;font-size:12px;color:#666}
.btn-add svg{fill:#888}
.search{position:absolute;left:338px;top:7px;width:215px;height:24px;display:flex}
.search-field{flex:1;border:1px solid #cfcfcf;background:#f7f7f7;font-size:10.5px;color:#777;padding:4px 11px}
.search-btn{width:28px;border:1px solid #cfcfcf;border-left:none;border-radius:0 3px 3px 0;background:linear-gradient(#fafafa,#e3e3e3);display:flex;align-items:center;justify-content:center}

.drivers-table{margin-top:13px}
.table-head{height:31px;border:1px solid var(--line);background:linear-gradient(#fff,#f0f0f0);position:relative;font-size:12.5px;color:var(--link)}
.table-head span{position:absolute;top:8px}
.col-name{left:26px}.col-dept{left:241px}.col-action{left:481px}
.driver-row{position:relative;height:48px;border:1px solid #e2e2e2;margin-top:3.4px}
.driver-photo{position:absolute;left:11px;top:7px;width:35px;height:32px;background:linear-gradient(135deg,#3d4a52,#7a6c5f 60%,#b9b2a6)}
.driver-name{position:absolute;left:58px;top:7px;font-size:12.5px;color:var(--link)}
.driver-meta{position:absolute;left:58px;top:25px;font-size:9px;font-style:italic;color:#666}
.driver-dept{position:absolute;left:240px;top:10px;font-size:9px;line-height:15.5px;color:#555}
.driver-status{position:absolute;left:479px;top:15px;display:flex;align-items:center;gap:7px;font-size:9.5px;color:#666}

/* footer */
.site-footer{position:absolute;left:0;top:729px;width:1200px;height:69px;background:var(--footer)}
.copyright{position:absolute;left:183px;top:25px;font-size:11px;color:#f1f1f1}
.social{position:absolute;left:944px;top:23px;display:flex;gap:6px}
.social span{width:20px;height:20px;border-radius:50%;background:#6f7f98}
</style>
</head>
<body>
<div class="page">

  <header class="site-header">
    <div class="brand"><span class="brand-mark"></span><span class="brand-name">HaulwaveKenro</span></div>
    <div class="header-btn btn-alerts">
      <svg width="10" height="11" viewBox="0 0 10 11"><path d="M5 0a1 1 0 011 1c2 .5 2.5 2 2.5 4v2l1.5 2H0l1.5-2V5C1.5 3 2 1.5 4 1a1 1 0 011-1zM3.8 10h2.4a1.2 1.2 0 01-2.4 0z"/></svg>
      Alerts : 0.00
    </div>
    <div class="header-btn btn-account">
      <svg width="10" height="11" viewBox="0 0 10 11"><circle cx="5" cy="3" r="2.8"/><path d="M0 11c0-3 2-4.5 5-4.5s5 1.5 5 4.5z"/></svg>
      Your Account
      <svg width="7" height="5" viewBox="0 0 7 5"><path d="M0 0h7L3.5 5z"/></svg>
    </div>
  </header>

  <nav class="main-nav">
    <div class="nav-item is-active">
      <svg viewBox="0 0 26 26"><circle cx="13" cy="13" r="10"/><path d="M13 13l5-4M7 13h1M18 13h1M13 7v1"/></svg>
      <span>Dashboard</span>
    </div>
    <div class="nav-item" style="left:352px">
      <svg viewBox="0 0 26 26"><circle cx="13" cy="6" r="3.5"/><path d="M6 23v-7a4 4 0 014-4h6a4 4 0 014 4v7z"/><circle cx="13" cy="18" r="2.5"/></svg>
      <span>Drivers</span>
    </div>
    <div class="nav-item" style="left:451px">
      <svg viewBox="0 0 26 26"><path d="M2 6h14v12H2zM16 10h5l3 4v4h-8z"/><circle cx="7" cy="20" r="2.2"/><circle cx="19" cy="20" r="2.2"/></svg>
      <span>Vehicles</span>
    </div>
    <div class="nav-item" style="left:545px">
      <svg viewBox="0 0 26 26"><path d="M5 23V4h10v19M5 11h10M15 9l4 3v8a2 2 0 004 0V9l-3-3"/></svg>
      <span>Fuel</span>
    </div>
    <div class="nav-item" style="left:645px">
      <svg viewBox="0 0 26 26"><circle cx="13" cy="13" r="10.5"/><circle cx="13" cy="13" r="6"/><path d="M13 7v12M7 13h12M9 9l8 8M17 9l-8 8"/></svg>
      <span>Tyres</span>
    </div>
    <div class="nav-item" style="left:735px">
      <svg viewBox="0 0 26 26"><path d="M6 4h14v20H6zM10 2h6v4h-6zM9 11l2 2 3-3M9 18l2 2 3-3"/></svg>
      <span>Tasks</span>
    </div>
    <div class="nav-item" style="left:833px">
      <svg viewBox="0 0 26 26"><circle cx="9" cy="16" r="4.5"/><circle cx="9" cy="16" r="1.5"/><circle cx="18" cy="8" r="3.5"/><circle cx="18" cy="8" r="1"/></svg>
      <span>Maintenance</span>
    </div>
    <div class="nav-item" style="left:949px">
      <svg viewBox="0 0 26 26"><path d="M3 24h21M5 24V3h4v21M11 24V12h4v12M17 24v-6h4v6"/></svg>
      <span>States &amp; Reports</span>
    </div>
  </nav>

  <aside class="sidebar">
    <div class="sidebar-title">Drivers</div>
    <div class="sidebar-link">Registered Drivers
      <svg width="11" height="9" viewBox="0 0 11 9"><path d="M0 0h2v1.5H0zM3 0h8v1.5H3zM0 2.5h2V4H0zM3 2.5h8V4H3zM0 5h2v1.5H0zM3 5h8v1.5H3zM0 7.5h2V9H0zM3 7.5h8V9H3z"/></svg>
    </div>
    <div class="sidebar-link">Add new driver
      <svg width="10" height="11" viewBox="0 0 10 11"><circle cx="5" cy="3" r="2.8"/><path d="M0 11c0-3 2-4.5 5-4.5s5 1.5 5 4.5z"/></svg>
    </div>
  </aside>

  <main class="content">
    <div class="toolbar">
      <div class="btn-add">
        <svg width="10" height="11" viewBox="0 0 10 11"><circle cx="5" cy="3" r="2.8"/><path d="M0 11c0-3 2-4.5 5-4.5s5 1.5 5 4.5z"/></svg>
        Add a new driver details
      </div>
      <div class="search">
        <div class="search-field">Search :</div>
        <div class="search-btn"><svg width="11" height="11" viewBox="0 0 11 11" fill="none" stroke="#666" stroke-width="1.6"><circle cx="4.5" cy="4.5" r="3.5"/><path d="M7 7l3.5 3.5"/></svg></div>
      </div>
    </div>

    <div class="drivers-table">
      <div class="table-head"><span class="col-name">Name of Driver</span><span class="col-dept">Department</span><span class="col-action">Action</span></div>

      <div class="driver-row"><div class="driver-photo" role="img" aria-label="Driver portrait photo"></div><div class="driver-name">Marlon Vesque</div><div class="driver-meta">27age, Driver</div><div class="driver-dept">Publishing packages and<br>web page editors</div><div class="driver-status"><svg width="16" height="15" viewBox="0 0 16 15"><rect x=".5" y="2.5" width="12" height="12" fill="#f4f4f4" stroke="#aaa"/><path d="M3 8l3 3 8-10" fill="none" stroke="#777" stroke-width="2"/></svg>Approved</div></div>
      <div class="driver-row"><div class="driver-photo" role="img" aria-label="Driver portrait photo"></div><div class="driver-name">Marlon Vesque</div><div class="driver-meta">27age, Driver</div><div class="driver-dept">Publishing packages and<br>web page editors</div><div class="driver-status"><svg width="16" height="15" viewBox="0 0 16 15"><rect x=".5" y="2.5" width="12" height="12" fill="#f4f4f4" stroke="#aaa"/><path d="M3 8l3 3 8-10" fill="none" stroke="#777" stroke-width="2"/></svg>Approved</div></div>
      <div class="driver-row"><div class="driver-photo" role="img" aria-label="Driver portrait photo"></div><div class="driver-name">Marlon Vesque</div><div class="driver-meta">27age, Driver</div><div class="driver-dept">Publishing packages and<br>web page editors</div><div class="driver-status"><svg width="16" height="15" viewBox="0 0 16 15"><rect x=".5" y="2.5" width="12" height="12" fill="#f4f4f4" stroke="#aaa"/><path d="M3 8l3 3 8-10" fill="none" stroke="#777" stroke-width="2"/></svg>Approved</div></div>
      <div class="driver-row"><div class="driver-photo" role="img" aria-label="Driver portrait photo"></div><div class="driver-name">Marlon Vesque</div><div class="driver-meta">27age, Driver</div><div class="driver-dept">Publishing packages and<br>web page editors</div><div class="driver-status"><svg width="16" height="15" viewBox="0 0 16 15"><rect x=".5" y="2.5" width="12" height="12" fill="#f4f4f4" stroke="#aaa"/><path d="M3 8l3 3 8-10" fill="none" stroke="#777" stroke-width="2"/></svg>Approved</div></div>
      <div class="driver-row"><div class="driver-photo" role="img" aria-label="Driver portrait photo"></div><div class="driver-name">Marlon Vesque</div><div class="driver-meta">27age, Driver</div><div class="driver-dept">Publishing packages and<br>web page editors</div><div class="driver-status"><svg width="16" height="15" viewBox="0 0 16 15"><rect x=".5" y="2.5" width="12" height="12" fill="#f4f4f4" stroke="#aaa"/><path d="M3 8l3 3 8-10" fill="none" stroke="#777" stroke-width="2"/></svg>Approved</div></div>
      <div class="driver-row"><div class="driver-photo" role="img" aria-label="Driver portrait photo"></div><div class="driver-name">Marlon Vesque</div><div class="driver-meta">27age, Driver</div><div class="driver-dept">Publishing packages and<br>web page editors</div><div class="driver-status"><svg width="16" height="15" viewBox="0 0 16 15"><rect x=".5" y="2.5" width="12" height="12" fill="#f4f4f4" stroke="#aaa"/><path d="M3 8l3 3 8-10" fill="none" stroke="#777" stroke-width="2"/></svg>Approved</div></div>
      <div class="driver-row"><div class="driver-photo" role="img" aria-label="Driver portrait photo"></div><div class="driver-name">Marlon Vesque</div><div class="driver-meta">27age, Driver</div><div class="driver-dept">Publishing packages and<br>web page editors</div><div class="driver-status"><svg width="16" height="15" viewBox="0 0 16 15"><rect x=".5" y="2.5" width="12" height="12" fill="#f4f4f4" stroke="#aaa"/><path d="M3 8l3 3 8-10" fill="none" stroke="#777" stroke-width="2"/></svg>Approved</div></div>
    </div>
  </main>

  <footer class="site-footer">
    <div class="copyright">Copyright 2013. Haulwavekenro. All Rights Reserved.</div>
    <div class="social"><span></span><span></span><span></span></div>
  </footer>

</div>
</body>
</html>
```